Sales Training Power Point Presentation

We are looking for a power point presentation that allows us to turn our training manual into a presentation. I am attaching the training manual here, just to give an idea of what we will be presenting. We want to be able to have graphs for some of that data and be able to move around slides/edit as we see it is needed.

Target Market(s)

new sales employees

Industry/Entity Type

staffing

Colors
0054AA
0677BA
7BADD7
CADEEF
E8F1F8
F0912C
F2A743
F7CA91
FBE8D2
FDF5EE

Requirements
Must have
• graphs

```html
<!DOCTYPE html>
<html lang="en">
<head>
<meta charset="utf-8">
<title>Sales Training Presentation</title>
<link href="https://fonts.googleapis.com/css2?family=Open+Sans:wght@400;600;700&display=swap" rel="stylesheet">
<style>
:root{
  --navy:#2d3a4c;
  --navy-dark:#232e3d;
  --orange:#ef6b2d;
  --orange-soft:#f5a06f;
  --yellow:#f6bb14;
  --grey:#9a9a9a;
  --page:#e2eaed;
  --light:#f1f1f1;
  --pale:#fdf1ea;
  --text:#333b47;
  --white:#ffffff;
}
*{box-sizing:border-box;margin:0;padding:0}
html,body{width:1200px;height:2400px;overflow:hidden;background:var(--page);font-family:"Open Sans",Arial,sans-serif;color:var(--text)}
.canvas{position:relative;width:1200px;height:2400px}
.slide{position:absolute;width:411px;height:231px;background:var(--white);overflow:hidden}
.col-a{left:174px}.col-b{left:615px}
.photo{position:absolute}
.ph-office{background:linear-gradient(135deg,#d9dcdc,#b7b2ab 55%,#8f8a84)}
.ph-warm{background:linear-gradient(135deg,#c9b8a6,#8c7a6a 60%,#5d5148)}
.ph-cool{background:linear-gradient(135deg,#9aa6b2,#5f6c7a 60%,#3b4654)}
.ph-dark{background:linear-gradient(135deg,#5c6672,#38414d)}
.brand{position:absolute;display:flex;align-items:center;gap:3px;font-weight:700;color:var(--navy);font-size:4.6px;letter-spacing:.4px;text-transform:uppercase}
.brand .dot{width:8px;height:8px;border-radius:50%;background:var(--orange)}
.brand.stack{flex-direction:column;gap:2px}
.brand.light{color:var(--white)}
.kicker{position:absolute;left:20px;top:15px;font-size:9px;color:var(--orange);text-transform:uppercase;line-height:1}
.title{position:absolute;left:20px;top:25px;font-size:13px;font-weight:700;color:var(--navy);text-transform:uppercase;line-height:1.1}
.body{position:absolute;font-size:5.2px;line-height:1.38}
.foot{position:absolute;left:0;bottom:0;width:100%;height:9px}
.foot .band{position:absolute;left:0;bottom:0;width:100%;height:6px;background:var(--navy)}
.foot .copy{position:absolute;left:20px;bottom:1.2px;font-size:3.4px;color:var(--white)}
.foot .tag{position:absolute;right:0;bottom:0;width:60px;height:9px;background:var(--orange);clip-path:polygon(14% 0,100% 0,100% 100%,0 100%);font-size:3.6px;color:var(--white);padding:2.5px 0 0 22px;letter-spacing:.3px}
.foot.plain .band{background:var(--orange)}
/* cover */
.cover{left:372px;top:39px;width:456px;height:257px;background:var(--navy)}
/* tables */
.tbl{position:absolute;border-collapse:collapse;font-size:4px;text-align:center;background:var(--white)}
.tbl th{font-weight:600;color:var(--white);height:13px;font-size:4.4px}
.tbl th.adv{background:var(--orange)}.tbl th.dis{background:var(--navy)}
.tbl td{height:15px;border-bottom:.5px solid #ddd;line-height:1.2;padding:0 2px}
/* cards */
.card{position:absolute;top:65px;width:113px;height:137px;background:var(--white);box-shadow:0 1px 3px rgba(0,0,0,.15)}
.card .img{position:absolute;left:2px;top:2px;width:109px;height:75px;border:2px solid var(--orange);border-bottom-width:0}
.card .cap{position:absolute;left:2px;top:50px;width:109px;text-align:center;color:var(--white);font-size:6px;line-height:1.2;text-transform:uppercase}
.card p{position:absolute;left:8px;top:90px;width:97px;text-align:center;font-size:5px;line-height:1.3}
/* steps */
.steps{position:absolute;left:0;top:49px;width:411px;height:15px;background:var(--navy);display:flex}
.steps div{flex:1;color:var(--white);font-size:6px;font-weight:600;text-align:center;line-height:15px}
.stepcol{position:absolute;top:72px;width:100px;text-align:center}
.stepcol h4{font-size:5.4px;color:var(--navy);margin:5px 0 16px;line-height:1.2}
.stepcol p{font-size:4.6px;line-height:1.3}
.tile{position:absolute;width:123px;height:64px;display:flex;align-items:center;justify-content:center;text-align:center;font-size:7px;line-height:1.2}
.num{display:inline-flex;width:9px;height:9px;border-radius:50%;background:var(--orange);color:#fff;font-size:5px;align-items:center;justify-content:center;margin-right:5px}
.member{position:absolute;top:65px;width:84px;text-align:center}
.member .pic{height:80px;clip-path:polygon(18% 0,100% 0,82% 100%,0 100%);border-top:3px solid var(--orange)}
.member .name{font-size:6px;font-weight:700;color:var(--orange);margin-top:4px}
.member .role{font-size:5px;margin-top:12px;line-height:1.3}
ul.bul{list-style:none}
ul.bul li{position:relative;padding-left:6px}
ul.bul li:before{content:"";position:absolute;left:0;top:2.4px;width:2px;height:2px;border-radius:50%;background:var(--orange)}
</style>
</head>
<body>
<div class="canvas">

<!-- Cover -->
<section class="slide cover">
  <div class="photo ph-office" style="left:180px;top:0;width:276px;height:257px;clip-path:polygon(30% 0,100% 0,100% 100%,55% 100%)" role="img" aria-label="Portrait of a smiling businesswoman in a white shirt with arms crossed"></div>
  <svg width="456" height="257" style="position:absolute;left:0;top:0">
    <polygon points="0,145 300,145 280,141 0,141" fill="var(--orange)"/>
    <polygon points="0,145 305,145 345,214 0,214" fill="var(--white)"/>
  </svg>
  <div class="brand stack light" style="left:20px;top:42px;font-size:8px"><span class="dot" style="width:22px;height:22px"></span>Corvant Group</div>
  <div style="position:absolute;left:20px;top:166px;font-size:26px;color:var(--navy)"><span style="color:var(--orange)">SALES</span> TRAINING</div>
  <div style="position:absolute;left:20px;top:225px;font-size:9px;color:var(--white)">July, 2023</div>
</section>

<!-- Title light -->
<section class="slide col-a" style="top:321px">
  <div class="photo ph-office" style="left:120px;top:0;width:291px;height:231px;clip-path:polygon(0 0,100% 0,100% 100%,90% 100%)" role="img" aria-label="Portrait of a smiling businesswoman in a white shirt"></div>
  <div class="brand stack" style="left:24px;top:17px;font-size:5.6px"><span class="dot" style="width:22px;height:22px"></span>Corvant Group</div>
  <div style="position:absolute;left:21px;top:75px;font-size:25px;line-height:1.15;color:var(--navy)"><span style="color:var(--orange)">SALES</span><br>TRAINING</div>
  <div style="position:absolute;left:21px;top:143px;background:var(--navy);color:#fff;font-size:7px;padding:2px 10px;border-radius:8px">July, 2023</div>
  <p class="body" style="left:21px;top:182px;width:220px;font-size:4.3px">Welcome to Corvant Talent's training guide to sales. We are very excited that you have joined our sales team. A career in sales is a worthwhile pursuit and our goal is to better arm you for success. We certainly believe our services are among the best in the industry and plan on continuing this legacy through the techniques outlined in this training course.</p>
  <div class="foot plain"><div class="band"></div><div class="copy">© Copyright Corvant Group</div></div>
</section>

<!-- Title dark -->
<section class="slide col-b" style="top:321px;background:var(--navy)">
  <div class="photo ph-office" style="left:120px;top:0;width:291px;height:231px;clip-path:polygon(0 0,100% 0,100% 100%,90% 100%)" role="img" aria-label="Portrait of a smiling businesswoman in a white shirt"></div>
  <div style="position:absolute;left:0;top:0;width:300px;height:231px;background:var(--navy);clip-path:polygon(0 0,40% 0,100% 100%,0 100%)"></div>
  <div class="brand stack light" style="left:24px;top:17px;font-size:5.6px"><span class="dot" style="width:22px;height:22px"></span>Corvant Group</div>
  <div style="position:absolute;left:21px;top:75px;font-size:25px;line-height:1.15;color:var(--white)"><span style="color:var(--orange)">SALES</span><br>TRAINING</div>
  <div style="position:absolute;left:21px;top:143px;background:var(--white);color:var(--navy);font-size:7px;padding:2px 10px;border-radius:8px">July, 2023</div>
  <p class="body" style="left:21px;top:182px;width:220px;font-size:4.3px;color:#fff">Welcome to Corvant Talent's training guide to sales. We are very excited that you have joined our sales team. A career in sales is a worthwhile pursuit and our goal is to better arm you for success. We certainly believe our services are among the best in the industry and plan on continuing this legacy through the techniques outlined in this training course.</p>
  <div class="foot plain"><div class="band"></div><div class="copy">© Copyright Corvant Group</div></div>
</section>

<!-- Table of contents -->
<section class="slide col-a" style="top:579px">
  <div class="photo ph-office" style="left:250px;top:0;width:161px;height:222px;clip-path:polygon(60% 0,100% 0,100% 100%,0 100%)" role="img" aria-label="Woman presenting at a whiteboard with charts"></div>
  <div class="brand stack light" style="left:370px;top:12px;font-size:3.6px"><span class="dot" style="width:8px;height:8px;background:#fff;opacity:.8"></span>Corvant Group</div>
  <div class="kicker">Table</div><div class="title">Of Contents</div>
  <div style="position:absolute;left:20px;top:52px;width:220px;font-size:5.6px;font-weight:600;color:var(--navy)">
    <div style="display:flex;justify-content:space-between;height:26.5px;border-bottom:.5px solid #ccc;padding-top:8px"><span>INDUSTRY ACUMEN</span><span style="color:var(--orange);font-weight:400">4</span></div>
    <div style="display:flex;justify-content:space-between;height:26.5px;border-bottom:.5px solid #ccc;padding-top:8px"><span>CORVANT TALENT: VALUE PROPOSITION</span><span style="color:var(--orange);font-weight:400">9</span></div>
    <div style="display:flex;justify-content:space-between;height:26.5px;border-bottom:.5px solid #ccc;padding-top:8px"><span>SALES CYCLE</span><span style="color:var(--orange);font-weight:400">16</span></div>
    <div style="display:flex;justify-content:space-between;height:26.5px;border-bottom:.5px solid #ccc;padding-top:8px"><span>DAILY SALES ACTIVITY</span><span style="color:var(--orange);font-weight:400">45</span></div>
    <div style="display:flex;justify-content:space-between;height:26.5px;border-bottom:.5px solid #ccc;padding-top:8px"><span>SYSTEMS &amp; TOOLS</span><span style="color:var(--orange);font-weight:400">48</span></div>
    <div style="display:flex;justify-content:space-between;height:26.5px;padding-top:8px"><span>BUSINESS PLANS</span><span style="color:var(--orange);font-weight:400">56</span></div>
  </div>
  <div class="foot"><div class="band"></div><div class="copy">© Copyright Corvant Group</div><div class="tag">PAGE 4</div></div>
</section>

<!-- Staffing industry with pie -->
<section class="slide col-b" style="top:579px">
  <div class="brand stack" style="left:368px;top:12px"><span class="dot"></span>Corvant Group</div>
  <div class="kicker">Staffing</div><div class="title">And Recruiting Industry</div>
  <div class="body" style="left:20px;top:48px;width:165px;font-size:5px;line-height:1.3">
    <p>While years back, employment agency (direct) placement fees were primarily paid for by the applicant (candidate). Today, the client companies pay most all employment agencies fees.</p>
    <p>(Average direct placement fee: 25% of candidate's annual salary)The temporary help service industry has the majority of customers.</p>
    <p style="margin-top:2px">In <b>2018</b>, revenues in staffing were <b style="color:var(--orange);font-size:7px">$167 Billion.</b></p>
    <p style="margin-top:2px">According to the National Staffing Council, over 90% of USA companies utilize temporary help.</p>
  </div>
  <div style="position:absolute;left:0;top:155px;width:192px;height:52px;background:var(--orange);display:flex;color:#fff;font-size:4.8px">
    <div style="flex:1;padding:8px 0 0 20px;border-right:.5px solid rgba(255,255,255,.6);margin:6px 0"><svg width="16" height="14" viewBox="0 0 16 14"><circle cx="8" cy="7" r="5" fill="none" stroke="#fff" stroke-width="1"/><circle cx="8" cy="7" r="1.5" fill="#fff"/></svg><br>Project<br>Initiatives</div>
    <div style="flex:1.4;padding:8px 0 0 8px;border-right:.5px solid rgba(255,255,255,.6);margin:6px 0"><svg width="16" height="14" viewBox="0 0 16 14"><rect x="3" y="6" width="10" height="7" fill="none" stroke="#fff"/><circle cx="8" cy="3" r="2.5" fill="none" stroke="#fff"/></svg><br>Companies with<br>limited capital</div>
    <div style="flex:1.2;padding:8px 0 0 8px;margin:6px 0"><svg width="16" height="14" viewBox="0 0 16 14"><circle cx="8" cy="7" r="5" fill="none" stroke="#fff"/><path d="M5 7l2 2 4-4" fill="none" stroke="#fff"/></svg><br>Need for quick<br>turnaround</div>
  </div>
  <div style="position:absolute;left:192px;top:48px;width:219px;height:160px;box-shadow:0 0 4px rgba(0,0,0,.15)">
    <svg width="219" height="160" viewBox="0 0 219 160" role="img" aria-label="Pie chart of four categories">
      <g transform="translate(110,68)">
        <path d="M0 0 L0 -57 A57 57 0 0 1 53.6 19.5 Z" fill="var(--orange)"/>
        <path d="M0 0 L53.6 19.5 A57 57 0 0 1 9.9 56.1 Z" fill="var(--navy)"/>
        <path d="M0 0 L9.9 56.1 A57 57 0 0 1 -55.4 13.5 Z" fill="var(--grey)"/>
        <path d="M0 0 L-55.4 13.5 A57 57 0 0 1 0 -57 Z" fill="var(--yellow)"/>
        <g font-size="8" fill="#fff" font-family="Open Sans,sans-serif"><text x="15" y="-12">430%</text><text x="15" y="28">250%</text><text x="-29" y="38">350%</text><text x="-40" y="-15" fill="#333">450%</text></g>
      </g>
      <g font-size="4.4" fill="#333" font-family="Open Sans,sans-serif">
        <rect x="38" y="136" width="4" height="4" fill="var(--orange)"/><text x="44" y="139.5">Category 1</text>
        <rect x="76" y="136" width="4" height="4" fill="var(--navy)"/><text x="82" y="139.5">Category 2</text>
        <rect x="114" y="136" width="4" height="4" fill="var(--grey)"/><text x="120" y="139.5">Category 3</text>
        <rect x="152" y="136" width="4" height="4" fill="var(--yellow)"/><text x="158" y="139.5">Category 4</text>
      </g>
    </svg>
  </div>
  <div class="foot"><div class="band"></div><div class="copy">© Copyright Corvant Group</div><div class="tag">PAGE 5</div></div>
</section>

<!-- Industry acumen -->
<section class="slide col-a" style="top:835px">
  <div class="brand stack" style="left:368px;top:12px"><span class="dot"></span>Corvant Group</div>
  <div class="kicker">Industry</div><div class="title">Acumen</div>
  <p class="body" style="left:20px;top:53px;width:120px;font-size:4.9px;line-height:1.3">For over a century the staffing industry has been called upon to help employers locate employees and vise/versa. As time has passed and business has grown more and more complex, staffing companies have both increased their size and scope. Now, the professional services or staffing industry has been touted as one of the fastest growing sectors in the business community. After many years of being almost exclusively linked to low level temp positions and general laborers, recruitment firms can now be found in 85% of the total job market. The following outlines some additional fact and figures:</p>
  <p class="body" style="left:156px;top:53px;font-size:5px">The Staffing Industry is made up of the following types of firms:</p>
  <div style="position:absolute;left:156px;top:67px;width:233px;height:127px;display:flex">
    <div class="photo ph-cool" style="position:relative;flex:1" role="img" aria-label="Hands shaking over a desk"></div>
    <div class="photo ph-office" style="position:relative;flex:1" role="img" aria-label="Close-up of a business handshake"></div>
    <div class="photo ph-dark" style="position:relative;flex:1" role="img" aria-label="Woman with a headset at a call desk"></div>
    <div class="photo ph-cool" style="position:relative;flex:1" role="img" aria-label="Executive in a suit working on a laptop"></div>
  </div>
  <div style="position:absolute;left:156px;top:175px;width:233px;display:flex;font-size:4.4px;color:#fff;text-align:center;line-height:1.2">
    <div style="flex:1">Contract<br>Services Firm</div><div style="flex:1">Direct Placement<br>Firms</div><div style="flex:1">Blended Services<br>(Contract / Direct<br>Placement Firms)</div><div style="flex:1">Executive Search<br>Firms (Retained<br>Search)</div>
  </div>
  <div class="foot"><div class="band"></div><div class="copy">© Copyright Corvant Group</div><div class="tag">PAGE 6</div></div>
</section>

<!-- Contract staffing arrangements -->
<section class="slide col-b" style="top:835px">
  <div class="photo ph-dark" style="left:0;top:0;width:411px;height:110px" role="img" aria-label="Business team meeting around a table"></div>
  <div style="position:absolute;left:0;top:0;width:411px;height:110px;background:rgba(45,58,76,.75)"></div>
  <div class="brand stack light" style="left:368px;top:12px"><span class="dot"></span>Corvant Group</div>
  <div style="position:absolute;left:0;top:27px;width:411px;text-align:center;font-size:8px;color:var(--orange);line-height:1">CONTRACT</div>
  <div style="position:absolute;left:0;top:38px;width:411px;text-align:center;font-size:13px;font-weight:600;color:#fff">STAFFING ARRANGEMENTS</div>
  <div class="card" style="left:21px"><div class="img ph-cool"></div><div class="cap">What is contract<br>staffing?</div><p>When a staffing firm provides leased employees on an "as needed" basis to accomplish project based objectives.</p></div>
  <div class="card" style="left:147px"><div class="img ph-warm"></div><div class="cap">What is full time<br>staffing?</div><p>When a staffing firm sources potential candidates that the clients wish to hire directly for full-time employment.</p></div>
  <div class="card" style="left:273px"><div class="img ph-office"></div><div class="cap">Who hires accounting<br>professionals?</div><p>Any firm that that has an Accounting and/or Finance department.</p></div>
  <div class="foot"><div class="band"></div><div class="copy">© Copyright Corvant Group</div><div class="tag">PAGE 7</div></div>
</section>

<!-- Full time staffing -->
<section class="slide col-a" style="top:1091px">
  <div style="position:absolute;left:0;top:45px;width:411px;height:170px;background:var(--light)"></div>
  <div class="brand stack" style="left:368px;top:12px"><span class="dot"></span>Corvant Group</div>
  <div class="kicker">Full Time</div><div class="title">Staffing</div>
  <div class="body" style="left:20px;top:87px;width:80px;font-size:6.8px;line-height:1.25">
    <div style="color:var(--orange)">Definition:</div><div>The hiring of employees on a full time basis.</div>
    <div style="color:var(--orange);margin-top:3px">Reason:</div><div>Long term employee need for a specific position.</div>
  </div>
  <svg style="position:absolute;left:177px;top:52px" width="20" height="16" viewBox="0 0 20 16"><rect x="4" y="2" width="12" height="12" fill="none" stroke="var(--orange)"/><path d="M7 6h6M7 9h6" stroke="var(--orange)"/></svg>
  <svg style="position:absolute;left:320px;top:52px" width="20" height="16" viewBox="0 0 20 16"><rect x="3" y="4" width="12" height="10" fill="none" stroke="var(--orange)"/><circle cx="14" cy="11" r="4" fill="#fff" stroke="var(--orange)"/></svg>
  <div style="position:absolute;left:110px;top:69px;width:146px;text-align:center;font-size:7px;color:var(--navy)">Contract Staffing</div>
  <div style="position:absolute;left:254px;top:69px;width:136px;text-align:center;font-size:7px;color:var(--navy)">Full Time Staffing</div>
  <table class="tbl" style="left:110px;top:80px;width:137px">
    <tr><th class="adv">ADVANTAGES</th><th class="dis">DISADVANTAGES</th></tr>
    <tr><td>Streamline #<br>of Employees</td><td>Lower Company Loyalty</td></tr>
    <tr><td>Hired Expertise</td><td>Cost for Specific<br>Talent / Rate</td></tr>
    <tr><td>Reduce<br>Training Costs</td><td>Short Term<br>Solution</td></tr>
    <tr><td>Flexibility<br>w/ Employees</td><td></td></tr>
    <tr><td>Overall Cost Saving<br>(Time / $)</td><td></td></tr>
  </table>
  <table class="tbl" style="left:254px;top:80px;width:137px">
    <tr><th class="adv">ADVANTAGES</th><th class="dis">DISADVANTAGES</th></tr>
    <tr><td>Can Create<br>Company Loyalty</td><td>Long Term<br>Commitment</td></tr>
    <tr><td>Long Term Staffing<br>Solutions / Team</td><td>Extensive Hiring Costs /<br>Onboarding</td></tr>
    <tr><td>Groom<br>in Management</td><td>Approval<br>Process</td></tr>
    <tr><td>Cost for<br>Specific Talent</td><td>Flexibility in Employee<br>Resources</td></tr>
    <tr><td></td><td></td></tr>
  </table>
  <div class="foot"><div class="band"></div><div class="copy">© Copyright Corvant Group</div><div class="tag">PAGE 8</div></div>
</section>

<!-- Value proposition -->
<section class="slide col-b" style="top:1091px">
  <div class="brand stack" style="left:368px;top:12px"><span class="dot"></span>Corvant Group</div>
  <div class="kicker">Corvant</div><div class="title">Value Proposition</div>
  <div class="photo ph-warm" style="left:21px;top:52px;width:135px;height:86px" role="img" aria-label="Team collaborating at a laptop"></div>
  <div class="photo ph-cool" style="left:66px;top:126px;width:116px;height:75px;border:3px solid #fff" role="img" aria-label="Businesswoman thinking at her desk"></div>
  <div class="body" style="left:160px;top:56px;width:240px;font-size:4.9px;line-height:1.3;text-align:center">
    <p>Now that we know what types of services we provide, it is imperative to separate ourselves from the competition. We separate ourselves by the value we provide. We interviewed our clients to determine what is valued by them. The results from the investigation were obvious.</p>
    <p style="margin-top:2px">Finding the best person for the job was valued most by our clients. This influenced how we would setup and position our organization. We accomplish this by the following methods:</p>
  </div>
  <div class="body" style="left:192px;top:133px;font-size:5.4px;line-height:1">
    <div style="height:15px"><span class="num">1</span>Defining and Communicating Corvant's Value Proposition</div>
    <div style="height:15px"><span class="num">2</span>Defining and Communicating YOUR Value Proposition</div>
    <div style="height:15px"><span class="num">3</span>Accomplishing Corvant's Value Proposition</div>
    <div style="height:15px"><span class="num">4</span>Proving Corvant's Value Proposition</div>
  </div>
  <div class="foot"><div class="band"></div><div class="copy">© Copyright Corvant Group</div><div class="tag">PAGE 9</div></div>
</section>

<!-- Accomplishing value proposition -->
<section class="slide col-a" style="top:1347px">
  <div class="brand stack" style="left:368px;top:12px"><span class="dot"></span>Corvant Group</div>
  <div class="kicker">Accomplishing</div><div class="title">Corvant's Value Proposition</div>
  <div class="steps"><div>STEP 1</div><div>STEP 2</div><div>STEP 3</div><div>STEP 4</div></div>
  <svg style="position:absolute;left:0;top:64px" width="411" height="150"><g stroke="#ddd" stroke-width=".6"><line x1="108" y1="0" x2="108" y2="140"/><line x1="212" y1="0" x2="212" y2="140"/><line x1="308" y1="0" x2="308" y2="140"/></g>
    <g fill="var(--orange)"><polygon points="50,0 58,0 54,5"/><polygon points="150,0 158,0 154,5"/><polygon points="253,0 261,0 257,5"/><polygon points="352,0 360,0 356,5"/></g></svg>
  <div class="stepcol" style="left:4px"><svg width="20" height="20" viewBox="0 0 20 20"><circle cx="10" cy="6" r="4" fill="none" stroke="var(--orange)"/><path d="M3 18c0-5 14-5 14 0" fill="none" stroke="var(--orange)"/></svg><h4>YOU</h4><p>You are responsible for the delivery of your product. Accountability starts and stops with you. Are you taking great requirements? Are we sending over "A" candidates? Do we understand what the customer wants? Etc.........</p></div>
  <div class="stepcol" style="left:110px"><svg width="20" height="20" viewBox="0 0 20 20"><circle cx="10" cy="10" r="4" fill="none" stroke="var(--orange)"/><circle cx="3" cy="4" r="2" fill="none" stroke="var(--orange)"/><circle cx="17" cy="4" r="2" fill="none" stroke="var(--orange)"/><circle cx="10" cy="18" r="1.5" fill="var(--orange)"/></svg><h4>Experience</h4><p>Nothing can replace experience and nothing is more vital to reducing the risk of potential candidates NOT being successful with our clients. Our organization has been creating success models for both candidates and clients for over 15 years.</p></div>
  <div class="stepcol" style="left:212px"><svg width="20" height="20" viewBox="0 0 20 20"><circle cx="8" cy="6" r="3.5" fill="none" stroke="var(--orange)"/><path d="M2 18c0-5 12-5 12 0" fill="none" stroke="var(--orange)"/><circle cx="15" cy="14" r="3" fill="none" stroke="var(--orange)"/></svg><h4 style="margin-bottom:10px">Our Internal<br>Recruiting Procedures</h4><p>Success Profiling our customers and consultants (ID Perfect Candidate) Sourcing the most viable candidates (Sourcing) 8 Step Screening Process (Screening) Retaining Current Consultants (Retaining)</p></div>
  <div class="stepcol" style="left:308px"><svg width="20" height="20" viewBox="0 0 20 20"><path d="M2 9l5-4 4 3 4-3 4 4-7 6z" fill="none" stroke="var(--orange)"/></svg><h4 style="margin-bottom:10px">Strategic<br>Partnerships</h4><p>Success Profiling our customers and consultants (ID Perfect Candidate) Sourcing the most viable candidates (Sourcing) 8 Step Screening Process (Screening) Retaining Current Consultants (Retaining)</p></div>
  <div class="foot"><div class="band"></div><div class="copy">© Copyright Corvant Group</div><div class="tag">PAGE 10</div></div>
</section>

<!-- Sales cycle -->
<section class="slide col-b" style="top:1347px">
  <div style="position:absolute;left:0;top:0;width:152px;height:215px;background:var(--light)"></div>
  <div class="brand stack" style="left:368px;top:12px"><span class="dot"></span>Corvant Group</div>
  <div class="kicker">The Sales</div><div class="title">Cycle<br>Company</div>
  <p class="body" style="left:21px;top:72px;width:118px;font-size:5.4px;line-height:1.3">What is territory knowledge and why is it important? We answer that question with the end goal in mind. TO MAKE PLACEMENTS!!!!!! With every end there has to be a beginning. Whether you are launching a new market or maintaining an existing territory, the speed and your ability to know your territory determines where your resource of time must be spent.</p>
  <svg style="position:absolute;left:185px;top:22px" width="190" height="190" viewBox="0 0 190 190" role="img" aria-label="Four-phase sales cycle wheel">
    <circle cx="95" cy="95" r="88" fill="var(--navy)"/>
    <path d="M95 7 A88 88 0 0 1 157 33 L120 70 A35 35 0 0 0 70 70 L33 33 A88 88 0 0 1 95 7Z" fill="var(--orange)"/>
    <path d="M95 183 A88 88 0 0 1 33 157 L70 120 A35 35 0 0 0 120 120 L157 157 A88 88 0 0 1 95 183Z" fill="var(--orange)"/>
    <g stroke="#fff" stroke-width="4"><line x1="33" y1="33" x2="70" y2="70"/><line x1="157" y1="33" x2="120" y2="70"/><line x1="33" y1="157" x2="70" y2="120"/><line x1="157" y1="157" x2="120" y2="120"/></g>
    <circle cx="95" cy="95" r="30" fill="#fff"/>
    <circle cx="95" cy="95" r="14" fill="none" stroke="var(--orange)" stroke-width="2"/>
    <g fill="var(--navy)"><rect x="88" y="95" width="3" height="7"/><rect x="93" y="91" width="3" height="11"/><rect x="98" y="88" width="3" height="14"/></g>
    <g font-family="Open Sans,sans-serif" text-anchor="middle" fill="#fff">
      <rect x="80" y="17" width="30" height="9" rx="4.5" fill="var(--orange-soft)"/><text x="95" y="24" font-size="5">PHASE 1</text>
      <text x="95" y="38" font-size="7" font-weight="700">PROSPECTING</text><text x="95" y="45" font-size="4.5">(Market Research)</text>
      <rect x="80" y="139" width="30" height="9" rx="4.5" fill="var(--orange-soft)"/><text x="95" y="146" font-size="5">PHASE 3</text>
      <text x="95" y="158" font-size="7" font-weight="700">OBTAINING</text><text x="95" y="166" font-size="7" font-weight="700">BUSINESS</text><text x="95" y="173" font-size="4.5">(Service Delivery)</text>
      <rect x="142" y="74" width="30" height="9" rx="4.5" fill="var(--orange)"/><text x="157" y="81" font-size="5">PHASE 2</text>
      <text x="157" y="93" font-size="6.5" font-weight="700">ACCOUNT</text><text x="157" y="101" font-size="6.5" font-weight="700">PENETRATION</text><text x="157" y="108" font-size="4.5">(Company Research)</text>
      <rect x="18" y="74" width="30" height="9" rx="4.5" fill="var(--orange)"/><text x="33" y="81" font-size="5">PHASE 4</text>
      <text x="33" y="93" font-size="6.5" font-weight="700">ACCOUNT</text><text x="33" y="101" font-size="6.5" font-weight="700">RETENTION</text><text x="33" y="108" font-size="4.5">(Maintanance)</text>
    </g>
  </svg>
  <div class="foot"><div class="band"></div><div class="copy">© Copyright Corvant Group</div><div class="tag">PAGE 11</div></div>
</section>

<!-- Phase 2 -->
<section class="slide col-a" style="top:1604px">
  <div class="brand stack" style="left:368px;top:12px"><span class="dot"></span>Corvant Group</div>
  <div class="kicker">Phase 2:</div><div class="title">Account Penetration</div>
  <p class="body" style="left:0;top:50px;width:411px;text-align:center;font-size:6.6px">The account penetration process is accomplished in the following steps:</p>
  <div class="tile ph-warm" style="left:21px;top:68px;background:linear-gradient(135deg,#f08a4c,#ef6b2d);color:#fff;font-size:9px" role="img" aria-label="Orange-tinted photo of people at work">Creating<br>Top 25</div>
  <div class="tile" style="left:144px;top:68px;background:var(--light)">Making First Contact / Cold<br>Calling / Setting Meetings</div>
  <div class="tile ph-cool" style="left:267px;top:68px;color:#fff;font-size:9px" role="img" aria-label="Grey-tinted photo of a business lunch">Lunches</div>
  <div class="tile" style="left:21px;top:132px;background:var(--white);box-shadow:0 0 3px rgba(0,0,0,.1)">Creating<br>Client Strategy</div>
  <div class="tile" style="left:144px;top:132px;background:linear-gradient(135deg,#3a4a60,#2d3a4c);color:#fff;font-size:9px" role="img" aria-label="Navy-tinted photo of a meeting">Running<br>Meetings</div>
  <div class="tile" style="left:267px;top:132px;background:var(--white);box-shadow:0 0 3px rgba(0,0,0,.1)">Follow Up<br>Communication Model</div>
  <div class="foot"><div class="band"></div><div class="copy">© Copyright Corvant Group</div><div class="tag">PAGE 12</div></div>
</section>

<!-- Business systems tools -->
<section class="slide col-b" style="top:1604px">
  <div style="position:absolute;left:0;top:0;width:110px;height:215px;background:var(--light)"></div>
  <div class="brand stack" style="left:368px;top:12px"><span class="dot"></span>Corvant Group</div>
  <div class="kicker">Business</div><div class="title">Ststems<br>Tools</div>
  <div class="body" style="left:21px;top:72px;width:84px;font-size:5.3px;line-height:1.3">
    <div style="font-weight:700;font-size:6px;margin-bottom:2px">1. MAILDESK:</div>
    MailDesk is one of the most powerful tools in your arsenal as a sale person. In this one product you can send / receive direct emails, sort correspondence for later use, keep track of appointments, file contacts, and even transfer information directly into your <b>A</b>pplicant <b>T</b>racking <b>S</b>ystem (ATS) or PlaceTrack.
  </div>
  <div class="photo" style="left:131px;top:40px;width:247px;height:154px;background:linear-gradient(180deg,#3e6fb8 0 6px,#e9eef5 6px);border:1px solid #9aa9bd" role="img" aria-label="Screenshot of an email and applicant tracking application"></div>
  <div class="foot"><div class="band"></div><div class="copy">© Copyright Corvant Group</div><div class="tag">PAGE 13</div></div>
</section>

<!-- Business tools alt -->
<section class="slide col-a" style="top:1860px">
  <div class="brand stack" style="left:368px;top:12px"><span class="dot"></span>Corvant Group</div>
  <div class="photo" style="left:21px;top:47px;width:213px;height:133px;background:linear-gradient(180deg,#3e6fb8 0 6px,#e9eef5 6px);border:1px solid #9aa9bd" role="img" aria-label="Screenshot of an email and applicant tracking application"></div>
  <div class="kicker" style="left:251px;top:58px">Business</div><div class="title" style="left:251px;top:68px">Ststems Tools</div>
  <div class="body" style="left:251px;top:92px;width:140px;font-size:5.3px;line-height:1.3">
    <div style="font-size:6px;margin-bottom:2px">1. MAILDESK:</div>
    MailDesk is one of the most powerful tools in your arsenal as a sale person. In this one product you can send / receive direct emails, sort correspondence for later use, keep track of appointments, file contacts, and even transfer information directly into your <b>A</b>pplicant <b>T</b>racking <b>S</b>ystem (ATS) or PlaceTrack.
  </div>
  <div class="foot"><div class="band"></div><div class="copy">© Copyright Corvant Group</div><div class="tag">PAGE 14</div></div>
</section>

<!-- Services staffing solutions -->
<section class="slide col-b" style="top:1860px">
  <div class="photo ph-cool" style="left:250px;top:30px;width:161px;height:175px;clip-path:polygon(12% 0,100% 0,100% 100%,0 100%)" role="img" aria-label="Business team discussing around a laptop"></div>
  <div class="brand stack" style="left:368px;top:12px"><span class="dot"></span>Corvant Group</div>
  <div class="kicker">Services</div><div class="title">Staffing Solutions</div>
  <p class="body" style="left:21px;top:43px;width:195px;font-size:6px;line-height:1.3">In fast paced business environment, there aren't always enough resources to properly address complex business challenges. You need the right resources at the right time, which are different at every stage. Corvant Group's network of professionals have the skills and expertise to help.</p>
  <div class="body" style="left:0;top:116px;width:250px;height:74px;background:var(--pale);padding:4px 0 0 21px;font-size:5.6px;line-height:1.35">
    <div style="font-size:6px;margin-bottom:1px">Managed Services by Corvant Group, provides you with:</div>
    <ul class="bul"><li>Subject matter experts to tackle every need</li><li>Customized team of specialists and support staff</li><li>Flexibility and scalability</li><li>Improved business performance</li><li>Partner for major business initiatives.</li></ul>
  </div>
  <div class="foot"><div class="band"></div><div class="copy">© Copyright Corvant Group</div><div class="tag">PAGE 15</div></div>
</section>

<!-- Our team -->
<section class="slide col-a" style="top:2118px">
  <div class="brand stack" style="left:368px;top:12px"><span class="dot"></span>Corvant Group</div>
  <div class="kicker">Our</div><div class="title">Team</div>
  <div class="member" style="left:22px"><div class="pic ph-cool" role="img" aria-label="Portrait of a founding partner"></div><div class="name">Daniel Mercer</div><div class="role">Founding Partner,<br>CEO</div></div>
  <div class="member" style="left:112px"><div class="pic ph-cool" role="img" aria-label="Portrait of a founding partner"></div><div class="name">Paul Whitford</div><div class="role">Founding Partner,<br>President</div></div>
  <div class="member" style="left:202px"><div class="pic ph-cool" role="img" aria-label="Portrait of a vice president"></div><div class="name">Laura Brennan</div><div class="role">Vice President,<br>Accounting &amp; Finance Division</div></div>
  <div class="member" style="left:292px"><div class="pic ph-cool" role="img" aria-label="Portrait of a director"></div><div class="name">Mark Delaney</div><div class="role">Director of Business Operations,<br>Technology Division</div></div>
  <div class="foot"><div class="band"></div><div class="copy">© Copyright Corvant Group</div><div class="tag">PAGE 17</div></div>
</section>

<!-- Closing -->
<section class="slide col-b" style="top:2118px;background:var(--navy)">
  <div class="photo ph-warm" style="left:0;top:0;width:280px;height:231px;clip-path:polygon(0 0,42% 0,100% 100%,0 100%)" role="img" aria-label="Businessman presenting to a team in a meeting room"></div>
  <div style="position:absolute;left:0;top:0;width:411px;height:231px;background:var(--orange);clip-path:polygon(44% 0,44.8% 0,68.8% 100%,68% 100%)"></div>
  <div class="brand stack light" style="left:295px;top:22px;font-size:8px"><span class="dot" style="width:20px;height:20px"></span>Corvant Group</div>
  <p class="body" style="left:230px;top:68px;width:170px;text-align:center;color:#fff;font-size:5.9px;line-height:1.3">Lorem Ipsum is simply dummy text of the printing and typesetting industry. Lorem Ipsum has been the industry's standard dummy text ever since the 1500s, when an unknown printer took a galley of type and scrambled it to make a type specimen book.</p>
  <div style="position:absolute;left:265px;top:150px;width:146px;height:46px;background:#fff;display:flex;font-size:5px;text-align:center">
    <div style="flex:1;padding-top:9px;border-right:.5px solid #ccc;margin:4px 0"><svg width="10" height="8" viewBox="0 0 10 8"><rect x=".5" y=".5" width="9" height="7" fill="none" stroke="var(--orange)"/><path d="M.5 .5l4.5 4 4.5-4" fill="none" stroke="var(--orange)"/></svg><br>Lorem ipsum</div>
    <div style="flex:1;padding-top:9px;border-right:.5px solid #ccc;margin:4px 0"><svg width="10" height="10" viewBox="0 0 10 10"><circle cx="5" cy="5" r="4.5" fill="var(--orange)"/></svg><br>Lorem ipsum</div>
    <div style="flex:1;padding-top:9px;margin:4px 0"><svg width="8" height="10" viewBox="0 0 8 10"><path d="M4 10C1 6 0 4.5 0 3.5a4 4 0 0 1 8 0C8 4.5 7 6 4 10z" fill="var(--orange)"/><circle cx="4" cy="3.5" r="1.4" fill="#fff"/></svg><br>Lorem ipsum</div>
  </div>
  <div class="foot plain"><div class="band"></div><div class="copy">© Copyright Corvant Group</div></div>
</section>

</div>
</body>
</html>
```